Podiatry (services) Business Card

I need a business design for a New Podiatry Service.
the Podiatry services will include all aspects of podiatry including;
general podiatry for all ages
corns and callus treatment
Ingrown toenails & nail surgery
Forefoot, arch and heel pain
Gait analysis
Sports Podiatry and Orthotics
Paediatric Assessments
Diabetes Foot Assessment

I would like the back of the card to have space for next appointment day and time.

I would like a nice design that is simple yet catchy. I don't like cluttered business cards. I like things to be simple yet stand out because of the finer details.

I like the colours blue and white but I'm open to other designs that have different colours.

Kestrel Podiatry (Business name)

Leisel Marrow - Podiatrist
M.Pod.P., B.Hlth. Sci, MQFotA

Address: 58 Tolbrook Rd, Larkhill East Vic, 3198
Phone: (03) 9564 2718
Fax: (03) 9432 6581

```html
<!DOCTYPE html>
<html lang="en">
<head>
<meta charset="utf-8">
<title>Kestrel Podiatry – Business Card</title>
<link rel="stylesheet" href="https://fonts.googleapis.com/css2?family=Didact+Gothic&family=Libre+Baskerville:wght@400;700&display=swap">
<style>
  :root {
    --brand-blue: #3a5fae;
    --brand-blue-deep: #2f4f9c;
    --ink-blue: #2c4a94;
    --accent-blue: #4a8fd4;
    --paper: #ffffff;
    --backdrop: #eceef2;
    --rule: #2c4a94;
  }
  * { box-sizing: border-box; margin: 0; padding: 0; }
  html, body { width: 1200px; height: 789px; overflow: hidden; }
  body {
    background: var(--backdrop);
    font-family: "Didact Gothic", sans-serif;
    position: relative;
  }
  .card {
    position: absolute;
    width: 540px;
    height: 310px;
    background: var(--paper);
    box-shadow: 0 6px 18px rgba(20, 30, 60, 0.18);
    overflow: hidden;
  }
  .card--back { left: 40px; top: 160px; }
  .card--front { left: 620px; top: 320px; }

  /* Back of card */
  .back-panel {
    position: absolute; left: 0; top: 0;
    width: 100%; height: 232px;
    background: var(--brand-blue);
  }
  .wordmark {
    position: absolute;
    display: flex; align-items: center; gap: 14px;
    font-family: "Didact Gothic", sans-serif;
    white-space: nowrap;
  }
  .wordmark__dot {
    width: 18px; height: 18px; border-radius: 50%;
    flex: none;
  }
  .card--back .wordmark { left: 70px; top: 92px; font-size: 46px; color: var(--paper); }
  .card--back .wordmark__dot { background: var(--paper); }
  .appointment {
    position: absolute; left: 0; top: 232px; width: 100%; height: 78px;
    color: var(--ink-blue); font-size: 14px;
  }
  .appointment__label { position: absolute; left: 120px; top: 16px; }
  .appointment__field { position: absolute; display: flex; align-items: flex-end; gap: 6px; }
  .appointment__field--date { left: 168px; top: 38px; }
  .appointment__field--time { left: 330px; top: 16px; }
  .appointment__dots { width: 120px; border-bottom: 1.5px dotted var(--ink-blue); height: 12px; }

  /* Front of card */
  .card--front .wordmark { left: 30px; top: 38px; font-size: 30px; color: var(--ink-blue); }
  .card--front .wordmark__dot { background: var(--accent-blue); width: 14px; height: 14px; }
  .top-rule {
    position: absolute; left: 330px; top: 58px; width: 190px;
    border-top: 1.5px solid var(--rule);
  }
  .practitioner {
    position: absolute; right: 30px; top: 92px; text-align: right;
    font-family: "Libre Baskerville", serif;
  }
  .practitioner__name {
    font-weight: 700; font-size: 19px; color: var(--ink-blue);
    display: flex; align-items: center; justify-content: flex-end; gap: 10px;
  }
  .practitioner__role {
    font-size: 13px; color: var(--ink-blue); margin-top: 2px; margin-right: 36px;
    display: flex; align-items: center; justify-content: flex-end; gap: 4px;
  }
  .practitioner__role::before {
    content: ""; width: 52px; border-top: 1px solid var(--rule); margin-top: 8px;
  }
  .practitioner__creds { font-size: 12px; font-weight: 700; color: var(--accent-blue); margin-top: 6px; }
  .person-badge { width: 28px; height: 28px; flex: none; }
  .bands { position: absolute; left: 0; top: 0; }
  .contact {
    position: absolute; color: var(--paper);
    font-family: "Libre Baskerville", serif; font-size: 13px; line-height: 1.6;
  }
  .contact__row { display: flex; align-items: center; gap: 8px; }
  .contact__icon { width: 13px; height: 13px; flex: none; }
  .contact--phones { left: 30px; top: 250px; }
  .contact--address { left: 360px; top: 198px; width: 170px; line-height: 1.5; }
  .contact--address .contact__row { align-items: flex-start; }
</style>
</head>
<body>

  <section class="card card--back" aria-label="Card back">
    <div class="back-panel">
      <div class="wordmark"><span class="wordmark__dot"></span><span>Kestrel Podiatry</span></div>
    </div>
    <div class="appointment">
      <span class="appointment__label">Next appointment,</span>
      <div class="appointment__field appointment__field--date"><span>Date</span><span class="appointment__dots"></span></div>
      <div class="appointment__field appointment__field--time"><span>Time</span><span class="appointment__dots"></span></div>
    </div>
  </section>

  <section class="card card--front" aria-label="Card front">
    <svg class="bands" width="540" height="310" viewBox="0 0 540 310" aria-hidden="true">
      <polygon points="0,238 296,238 320,310 0,310" fill="var(--brand-blue)"/>
      <polygon points="312,178 540,178 540,310 356,310" fill="var(--brand-blue-deep)"/>
    </svg>

    <div class="wordmark"><span class="wordmark__dot"></span><span>Kestrel Podiatry</span></div>
    <div class="top-rule"></div>

    <div class="practitioner">
      <div class="practitioner__name">
        <span>Leisel Marrow</span>
        <svg class="person-badge" viewBox="0 0 28 28" aria-hidden="true">
          <circle cx="14" cy="14" r="13" fill="var(--accent-blue)"/>
          <circle cx="14" cy="10" r="4" fill="#fff"/>
          <path d="M7 21c0-4 3-6 7-6s7 2 7 6z" fill="#fff"/>
        </svg>
      </div>
      <div class="practitioner__role">Podiatrist</div>
      <div class="practitioner__creds">M.Pod.P., B.Hlth. Sci, MQFotA</div>
    </div>

    <div class="contact contact--phones">
      <div class="contact__row">
        <svg class="contact__icon" viewBox="0 0 16 16" aria-hidden="true">
          <circle cx="8" cy="8" r="8" fill="#fff"/>
          <path d="M5 4.5l1.5-.5 1 2-1 .8c.5 1 1.2 1.7 2.2 2.2l.8-1 2 1-.5 1.5c-3 .2-6.2-3-6-6z" fill="var(--brand-blue)"/>
        </svg>
        <span>(03) 9564 2718</span>
      </div>
      <div class="contact__row">
        <svg class="contact__icon" viewBox="0 0 16 16" aria-hidden="true">
          <circle cx="8" cy="8" r="8" fill="#fff"/>
          <rect x="5.5" y="3.8" width="5" height="2.6" fill="var(--brand-blue)"/>
          <rect x="4" y="6.8" width="8" height="4" rx="1" fill="var(--brand-blue)"/>
          <rect x="5.5" y="9.5" width="5" height="2.8" fill="var(--brand-blue)"/>
        </svg>
        <span>(03) 9432 6581</span>
      </div>
    </div>

    <div class="contact contact--address">
      <div class="contact__row">
        <svg class="contact__icon" viewBox="0 0 16 16" aria-hidden="true" style="margin-top:3px">
          <path d="M8 1a5 5 0 0 0-5 5c0 4 5 9 5 9s5-5 5-9a5 5 0 0 0-5-5z" fill="#fff"/>
          <circle cx="8" cy="6" r="2" fill="var(--brand-blue-deep)"/>
        </svg>
        <span>58 Tolbrook Rd, Larkhill East Vic, 3198</span>
      </div>
    </div>
  </section>

</body>
</html>
```